Event flyer for Sunday night Youth Group

Need a 4 x 6 or 5 x 7 flyer for a new youth group starting on April 14. The youth group is for students in middle school and high school so it needs to look fun and cool, but not childish. I prefer it not to include pictures of people unless it's so obscure you can't really see their faces. I've uploaded some pictures of flyers I like. I've also attached a couple versions of our logo to use on the flyer.
Information the flyer needs to include:
Youth Group
Sundays, 6-8pm (beginning April 14)
Location: Wexlander's - 4182 Quillon Ridge Ave N, Keizer, 97158
There will be dinner, games, friends, and a message.
Target Market(s)
Youth ages 13-18
Industry/Entity Type
Church
Colors
Look and feel

```html
<!DOCTYPE html>
<html lang="en">
<head>
<meta charset="utf-8">
<title>Youth Group Flyer</title>
<link rel="stylesheet" href="https://fonts.googleapis.com/css2?family=Titan+One&family=Yellowtail&family=Oswald:wght@500&family=Open+Sans:wght@300;400;700;800&display=block">
<style>
  :root {
    --backdrop: #d3cbc6;
    --ink-black: #050307;
    --title-red: #ec1c24;
    --title-yellow: #e9ec6a;
    --script-purple: #6a36b4;
    --script-edge: #efe9f7;
    --detail-yellow: #f3ef6c;
    --band-purple: rgba(52, 26, 88, 0.88);
    --white: #ffffff;
    --accent-yellow: #fff200;
    --stage-pink: #e01f86;
    --stage-violet: #4a1a6e;
    --crowd-bright: #4a6cf0;
    --crowd-blue: #3b3fc4;
    --crowd-deep: #1d1a5c;
  }
  * { margin: 0; padding: 0; box-sizing: border-box; }
  html, body {
    width: 1200px; height: 1024px; overflow: hidden;
    background: var(--backdrop);
  }
  .flyer {
    position: absolute; left: 250px; top: 17px;
    width: 700px; height: 990px;
    background: var(--ink-black);
    overflow: hidden;
  }
  .stage-photo {
    position: absolute; left: 0; top: 0; width: 100%; height: 380px;
    background:
      radial-gradient(ellipse 220px 150px at 330px 300px, var(--stage-pink) 0%, rgba(224,31,134,0.45) 55%, transparent 85%),
      radial-gradient(ellipse 200px 260px at 620px 60px, rgba(140,40,180,0.7) 0%, transparent 80%),
      linear-gradient(180deg, #1a0a18 0%, #3a1450 45%, var(--stage-violet) 75%, #5a1c78 100%);
  }
  .crowd-photo {
    position: absolute; left: 0; top: 400px; width: 100%; height: 480px;
    background:
      radial-gradient(ellipse 420px 170px at 330px 120px, rgba(90,150,255,0.55) 0%, transparent 80%),
      radial-gradient(ellipse 300px 140px at 560px 260px, rgba(80,110,240,0.45) 0%, transparent 80%),
      radial-gradient(ellipse 300px 140px at 120px 280px, rgba(70,90,220,0.45) 0%, transparent 80%),
      linear-gradient(180deg, var(--crowd-blue) 0%, var(--crowd-bright) 18%, #3a44c8 45%, #3a3694 65%, #2a2550 82%, var(--ink-black) 100%);
  }
  .title-youth {
    position: absolute; left: 60px; top: 55px;
    font-family: "Titan One", sans-serif; font-weight: 400;
    font-size: 132px; line-height: 1;
    color: var(--title-red);
    letter-spacing: -2px;
    transform: rotate(-7deg); transform-origin: left bottom;
    text-shadow:
      -2px 2px 0 var(--title-yellow), -4px 4px 0 var(--title-yellow),
      -6px 6px 0 var(--title-yellow), -8px 8px 0 var(--title-yellow),
      -10px 10px 0 var(--title-yellow), -12px 12px 0 var(--title-yellow);
  }
  .title-group {
    position: absolute; left: 250px; top: 170px;
    font-family: "Yellowtail", "Brush Script MT", cursive;
    font-size: 112px; line-height: 1;
    color: var(--script-purple);
    -webkit-text-stroke: 3px var(--script-edge);
    paint-order: stroke fill;
    transform: rotate(-16deg); transform-origin: left bottom;
  }
  .schedule {
    position: absolute; left: 372px; top: 272px; width: 260px;
    font-family: "Oswald", sans-serif; font-weight: 500;
    font-size: 32px; line-height: 1.15;
    color: var(--detail-yellow);
    text-align: center;
  }
  .location-band {
    position: absolute; left: 0; top: 365px; width: 100%; height: 62px;
    background: var(--band-purple);
    display: flex; align-items: center; justify-content: center; gap: 10px;
    color: var(--white);
  }
  .venue-name {
    font-family: "Open Sans", sans-serif; font-weight: 800; font-size: 30px;
  }
  .venue-address {
    font-family: "Open Sans", sans-serif; font-weight: 300; font-size: 20px;
  }
  .footer {
    position: absolute; left: 0; bottom: 0; width: 100%; height: 130px;
    display: flex; align-items: center; justify-content: space-between;
    padding: 0 38px 10px 38px;
  }
  .church-name {
    display: flex; align-items: center; gap: 14px;
    font-family: "Open Sans", sans-serif; font-weight: 400;
    font-size: 25px; letter-spacing: 2px; color: var(--white);
  }
  .church-mark { width: 28px; height: 28px; background: var(--white); }
  .invite {
    font-family: "Open Sans", sans-serif; font-weight: 400;
    font-size: 22px; line-height: 1.1; color: var(--white);
    text-align: right;
  }
  .invite-highlight {
    display: block;
    font-weight: 800; font-size: 30px; letter-spacing: 3px;
    color: var(--accent-yellow);
  }
</style>
</head>
<body>
  <main class="flyer">
    <div class="stage-photo" role="img" aria-label="Concert stage lit with pink and purple spotlights"></div>
    <div class="crowd-photo" role="img" aria-label="Large crowd in blue light seen from behind, faces not visible, fading into darkness"></div>

    <h1 class="title-youth">YOUTH</h1>
    <div class="title-group">Group</div>

    <p class="schedule">Sundays, 6-8pm<br>(beginning April 14)</p>

    <div class="location-band">
      <span class="venue-name">Wexlander's</span>
      <span class="venue-address">4182 Quillon Ridge Ave N, Keizer, 97158</span>
    </div>

    <footer class="footer">
      <div class="church-name"><span class="church-mark"></span>WAYFIELD FELLOWSHIP</div>
      <p class="invite">There will be dinner,<br>games, friends, and<span class="invite-highlight">a message</span></p>
    </footer>
  </main>
</body>
</html>
```